Business card

I need a business card design for my consulting company in animal welfare for livestock. I like clean, crisp, simple.

One I imagined was double-sided:
side1: just my name and contact information
side2: silhouette of farm animals. Could be 3 (pig, cow, chicken) or all the species (pig, cow, chicken, duck, sheep, rabbit, etc) that continue the length of the card. I have attached an image of a silhouette style.

But, I am open to any concept.

Industry/Entity Type

Business

```html
<!DOCTYPE html>
<html lang="en">
<head>
<meta charset="utf-8">
<title>Careful Services for Farmstead Partners — Business Card</title>
<link rel="stylesheet" href="https://fonts.googleapis.com/css2?family=Cinzel:wght@400;500&family=Open+Sans:wght@400;600&display=swap">
<style>
  :root {
    --stage: #2b2b2b;
    --card-white: #ffffff;
    --card-black: #000000;
    --ink: #111111;
    --blue: #2f6fbd;
    --silhouette: #e3e5f0;
    --white: #ffffff;
  }
  * { box-sizing: border-box; margin: 0; padding: 0; }
  html, body {
    width: 1200px; height: 900px; overflow: hidden;
    background: var(--stage);
  }
  .canvas { position: relative; width: 1200px; height: 900px; }

  .card {
    position: absolute;
    width: 700px; height: 400px;
    overflow: hidden;
    box-shadow: 0 12px 30px rgba(0,0,0,.45);
  }

  /* Front: contact side */
  .card--front { left: 90px; top: 40px; background: var(--card-white); }
  .front__animals {
    position: absolute; inset: 0;
    background: radial-gradient(ellipse at 30% 35%, var(--silhouette) 0%, rgba(227,229,240,0) 55%),
                radial-gradient(ellipse at 75% 75%, var(--silhouette) 0%, rgba(227,229,240,0) 45%);
    opacity: .8;
  }
  .brand {
    position: absolute; left: 60px; top: 70px;
    display: flex; flex-direction: column; align-items: flex-start; gap: 22px;
  }
  .brand__circle {
    width: 120px; height: 120px; border-radius: 50%;
    background: var(--ink);
    margin-left: 60px;
  }
  .brand__name {
    font-family: 'Cinzel', serif; font-weight: 500;
    font-size: 21px; line-height: 1.15; letter-spacing: .5px;
    color: var(--ink);
  }
  .contact {
    position: absolute; right: 50px; top: 110px;
    text-align: right;
  }
  .contact__name {
    font-family: 'Cinzel', serif; font-weight: 400;
    font-size: 24px; letter-spacing: 1px;
    color: var(--blue); margin-bottom: 10px;
  }
  .contact__line {
    font-family: 'Open Sans', sans-serif; font-size: 15px;
    color: var(--ink); line-height: 1.7;
  }
  .contact__label { color: var(--blue); font-weight: 600; margin-right: 4px; }
  .front__band {
    position: absolute; right: 0; top: 250px;
    width: 250px; height: 14px; background: var(--blue);
  }

  /* Back: brand side */
  .card--back { left: 410px; top: 470px; background: var(--card-black); }
  .back__circle {
    position: absolute; left: 250px; top: 60px;
    width: 190px; height: 190px; border-radius: 50%;
    background: var(--white);
  }
  .back__name {
    position: absolute; left: 0; right: 0; top: 275px;
    text-align: center;
    font-family: 'Cinzel', serif; font-weight: 500;
    font-size: 27px; line-height: 1.15; letter-spacing: .5px;
    color: var(--white);
  }
</style>
</head>
<body>
<main class="canvas">

  <section class="card card--front">
    <div class="front__animals" role="img" aria-label="Faint silhouettes of farm animals: horse, hen, cow, pig, rabbit and sheep"></div>

    <div class="brand">
      <span class="brand__circle"></span>
      <p class="brand__name">Careful Services for<br>Farmstead Partners</p>
    </div>

    <div class="contact">
      <p class="contact__name">Mara Ellwood</p>
      <p class="contact__line"><span class="contact__label">P:</span>+1.555.014.2290</p>
      <p class="contact__line"><span class="contact__label">E:</span>mara.ellwood@example.com</p>
    </div>

    <span class="front__band"></span>
  </section>

  <section class="card card--back">
    <span class="back__circle"></span>
    <p class="back__name">Careful Services for<br>Farmstead Partners</p>
  </section>

</main>
</body>
</html>
```